Copper lark buildworks

Copper lark buildworks is a small construction company.
Who is a licenced builder, Carpenter, joiner,
working on heritage ,new build, speacial projects and sometimes furniture

Industry/Entity Type

Construction

```html
<!DOCTYPE html>
<html lang="en">
<head>
<meta charset="UTF-8">
<title>Copper lark buildworks – Business Card</title>
<link href="https://fonts.googleapis.com/css2?family=Montserrat:wght@400;500;600&display=swap" rel="stylesheet">
<style>
  :root {
    --backdrop: #cfd0cf;
    --teal-deep: #5ea59b;
    --teal-light: #93d3c9;
    --panel-grey: #6b6f70;
    --panel-line: #a9dcd4;
    --ink: #ffffff;
    --globe: #efe6b8;
  }
  * { box-sizing: border-box; margin: 0; padding: 0; }
  html, body {
    width: 1200px;
    height: 1200px;
    overflow: hidden;
    background: var(--backdrop);
    font-family: "Montserrat", sans-serif;
  }
  .canvas {
    position: relative;
    width: 1200px;
    height: 1200px;
  }
  .business-card {
    position: absolute;
    left: 100px;
    top: 290px;
    width: 1000px;
    height: 620px;
    overflow: hidden;
    background: linear-gradient(120deg, var(--teal-deep) 0%, #74bcb1 45%, var(--teal-light) 75%, #7cc3b8 100%);
    box-shadow: 0 8px 24px rgba(0,0,0,0.18);
    color: var(--ink);
  }
  .card-art {
    position: absolute;
    inset: 0;
    width: 1000px;
    height: 620px;
  }
  .brand {
    position: absolute;
    left: 40px;
    top: 44px;
    display: flex;
    align-items: center;
    gap: 16px;
  }
  .brand-circle {
    width: 72px;
    height: 72px;
    border: 3px solid var(--ink);
    border-radius: 50%;
  }
  .brand-name {
    font-weight: 400;
    font-size: 24px;
    line-height: 1.05;
  }
  .holder {
    position: absolute;
    left: 180px;
    top: 250px;
  }
  .holder-name {
    font-weight: 600;
    font-size: 80px;
    line-height: 1;
    letter-spacing: -1px;
    white-space: nowrap;
  }
  .holder-role {
    text-align: right;
    font-weight: 500;
    font-size: 26px;
    margin-top: 2px;
  }
  .contact {
    position: absolute;
    display: flex;
    align-items: center;
    gap: 18px;
    font-size: 20px;
    font-weight: 400;
    white-space: nowrap;
  }
  .contact svg { width: 30px; height: 30px; flex: none; }
  .contact-website { left: 560px; top: 390px; }
  .contact-email   { left: 560px; top: 468px; }
  .contact-address { left: 190px; top: 470px; }
  .contact-phone   { left: 190px; top: 548px; }
</style>
</head>
<body>
<div class="canvas">
  <section class="business-card">
    <svg class="card-art" viewBox="0 0 1000 620">
      <line x1="490" y1="0" x2="708" y2="322" stroke="#ffffff" stroke-opacity="0.18" stroke-width="3"/>
      <polyline points="708,0 708,322 960,620"
                fill="none" stroke="var(--panel-line)" stroke-width="4"/>
      <polygon role="img" aria-label="Decorative grey arabesque ornament panel"
               points="722,0 1000,0 1000,620 990,620 722,314"
               fill="var(--panel-grey)"/>
    </svg>

    <div class="brand">
      <div class="brand-circle"></div>
      <div class="brand-name">Copper<br>lark<br>buildworks</div>
    </div>

    <div class="holder">
      <div class="holder-name">Your Name</div>
      <div class="holder-role">CO-Director</div>
    </div>

    <div class="contact contact-website">
      <svg viewBox="0 0 24 24" fill="none" stroke="var(--globe)" stroke-width="1.6">
        <circle cx="12" cy="12" r="10"/>
        <ellipse cx="12" cy="12" rx="4.5" ry="10"/>
        <line x1="2" y1="12" x2="22" y2="12"/>
        <path d="M4 7h16M4 17h16"/>
      </svg>
      <span>Website</span>
    </div>

    <div class="contact contact-email">
      <svg viewBox="0 0 24 24" fill="none" stroke="var(--ink)" stroke-width="1.8">
        <rect x="2" y="5" width="20" height="14"/>
        <path d="M2 5l10 8 10-8"/>
      </svg>
      <span>E-mail</span>
    </div>

    <div class="contact contact-address">
      <svg viewBox="0 0 24 24" fill="var(--ink)">
        <path d="M12 2a7 7 0 0 0-7 7c0 5 7 13 7 13s7-8 7-13a7 7 0 0 0-7-7zm0 9.5A2.5 2.5 0 1 1 12 6.5a2.5 2.5 0 0 1 0 5z"/>
      </svg>
      <span>Address</span>
    </div>

    <div class="contact contact-phone">
      <svg viewBox="0 0 24 24" fill="var(--ink)">
        <path d="M2 8c0-3 4-5 10-5s10 2 10 5v2h-5V8H7v2H2z"/>
        <path d="M5 12h14v9H5z"/>
        <circle cx="12" cy="16.5" r="2.5" fill="#6fb8ad"/>
      </svg>
      <span>Phone</span>
    </div>
  </section>
</div>
</body>
</html>
```